Lark and Fern: Prespective and Balence in People's Lives Needs a Buissness Card Design

Lark and Fern Community Center is an organization that seeks to bring balance into people's lives. Main services include: guided meditation, group brainstorming, and guided counseling. Lark and Fern combines Eastern practices, i.e. Buddhism, Hinduism, and Taoism, with Western practices: therapy, group brainstorming and healing. We would like a double sided card: 1) front vertical with image, 2) back horizontal with information. The main colors for the card are red, white, black. Different finishes would be nice--please no high gloss. Matte, pearlized, embossing--used tactfully and sparingly would be nice. The card should convey balance/harmony in a modern world.

```html
<!DOCTYPE html>
<html lang="en">
<head>
<meta charset="utf-8">
<title>Lark and Fern Community Center – Business Card</title>
<link rel="stylesheet" href="https://fonts.googleapis.com/css2?family=Lato:ital,wght@0,400;0,700;0,900;1,700&display=swap">
<style>
  :root {
    --red: #d10a11;
    --black: #111111;
    --white: #ffffff;
    --paper: #f4f4f4;
    --ink: #1a1a1a;
    --stage: #2e2e2e;
  }
  * { margin: 0; padding: 0; box-sizing: border-box; }
  html, body {
    width: 1200px; height: 997px; overflow: hidden;
    background: var(--stage);
    font-family: "Lato", Arial, sans-serif;
  }
  .canvas { position: relative; width: 1200px; height: 997px; }

  /* Front: vertical card */
  .card-front {
    position: absolute; left: 120px; top: 199px;
    width: 343px; height: 600px; overflow: hidden;
    background: var(--white);
    display: flex; flex-direction: column; align-items: center; justify-content: center;
    gap: 26px;
  }
  .front-mark {
    width: 120px; height: 120px; border-radius: 50%;
    background: var(--red);
  }
  .front-name {
    color: var(--black); font-weight: 900; font-size: 30px;
    text-transform: uppercase; letter-spacing: 0.5px; text-align: center;
  }

  /* Back: horizontal card */
  .card-back {
    position: absolute; left: 520px; top: 327px;
    width: 600px; height: 343px; overflow: hidden;
    background: var(--paper);
  }
  .back-info { position: absolute; left: 150px; top: 34px; width: 430px; }
  .org-name {
    color: var(--red); font-weight: 900; font-size: 19px;
    letter-spacing: 0.3px; text-transform: uppercase; text-align: center;
  }
  .tagline {
    color: var(--ink); font-weight: 700; font-style: italic; font-size: 17px;
    text-align: center; margin-top: 2px;
  }
  .person { margin-top: 22px; margin-left: 78px; }
  .person-name {
    color: var(--red); font-weight: 900; font-size: 18px; text-transform: uppercase;
  }
  .person-title {
    color: var(--ink); font-weight: 900; font-size: 13px; text-transform: uppercase;
    letter-spacing: 0.3px;
  }
  .contact-list { list-style: none; margin-top: 20px; margin-left: 78px; }
  .contact-item {
    display: flex; align-items: flex-start; gap: 8px;
    color: var(--ink); font-size: 14px; font-weight: 400; line-height: 17px;
    margin-bottom: 8px;
  }
  .contact-icon { flex: none; width: 18px; height: 18px; }
  .card-edge { position: absolute; left: 0; bottom: 0; }
</style>
</head>
<body>
<main class="canvas">

  <section class="card-front" aria-label="Card front">
    <div class="front-mark" aria-hidden="true"></div>
    <p class="front-name">Lark and Fern</p>
  </section>

  <section class="card-back" aria-label="Card back">
    <div class="back-info">
      <h1 class="org-name">Lark and Fern Community Center</h1>
      <p class="tagline">bring balance into people's lives</p>

      <div class="person">
        <h2 class="person-name">Dana Whitlow</h2>
        <p class="person-title">Managing Director</p>
      </div>

      <ul class="contact-list">
        <li class="contact-item">
          <svg class="contact-icon" viewBox="0 0 18 18" aria-hidden="true">
            <circle cx="9" cy="9" r="9" fill="var(--red)"/>
            <path d="M6 4.5 L7.6 4.5 L8.3 6.8 L7.2 7.7 Q8 9.6 10.3 10.8 L11.2 9.7 L13.5 10.4 L13.5 12 Q12.8 13.4 11 13.2 Q5.5 12 4.8 6.4 Q4.8 4.8 6 4.5 Z" fill="var(--white)"/>
          </svg>
          <span>416-555-0142</span>
        </li>
        <li class="contact-item">
          <svg class="contact-icon" viewBox="0 0 18 18" aria-hidden="true">
            <circle cx="9" cy="9" r="9" fill="var(--red)"/>
            <rect x="4.5" y="5.8" width="9" height="6.4" fill="none" stroke="var(--white)" stroke-width="1.2"/>
            <path d="M4.5 5.8 L9 9.4 L13.5 5.8" fill="none" stroke="var(--white)" stroke-width="1.2"/>
          </svg>
          <span>dana@larkandfern.org</span>
        </li>
        <li class="contact-item">
          <svg class="contact-icon" viewBox="0 0 18 18" aria-hidden="true">
            <circle cx="9" cy="9" r="9" fill="var(--red)"/>
            <rect x="4" y="7.6" width="5.5" height="3" rx="1.5" fill="none" stroke="var(--white)" stroke-width="1.2" transform="rotate(-45 6.75 9.1)"/>
            <rect x="8.5" y="7.4" width="5.5" height="3" rx="1.5" fill="none" stroke="var(--white)" stroke-width="1.2" transform="rotate(-45 11.25 8.9)"/>
          </svg>
          <span>larkandfern.example.org</span>
        </li>
        <li class="contact-item">
          <svg class="contact-icon" viewBox="0 0 18 18" aria-hidden="true">
            <circle cx="9" cy="9" r="9" fill="var(--red)"/>
            <path d="M9 14 Q5.2 9.6 5.2 7.6 A3.8 3.8 0 0 1 12.8 7.6 Q12.8 9.6 9 14 Z" fill="var(--white)"/>
            <circle cx="9" cy="7.6" r="1.4" fill="var(--red)"/>
          </svg>
          <span>118 Willowbank Road East<br>Suite 400, Canada</span>
        </li>
      </ul>
    </div>

    <svg class="card-edge" width="600" height="343" viewBox="0 0 600 343" aria-hidden="true">
      <path class="edge-red" d="M0 326 L440 312 L440 343 L0 343 Z" fill="var(--red)"/>
      <path class="edge-black" d="M440 343 L440 322 Q440 290 472 290 L600 290 L600 343 Z" fill="var(--black)"/>
    </svg>
  </section>

</main>
</body>
</html>
```